Local fast-growing company in the service sector

We are looking for a modern business card design, which should also appear on our letterheads

Target Market(s)

Private and industrial sectors

Contact Information for Business Card

Vorname Name
Lindkofer Str. 18
71468 Kernhausen
Tel.: 07163-418259-0
Name@kovaltec-pbz.de

Colors
9d9d9d
919191
aaaaaa

Requirements
Must have
• The logo (file) in silver

```html
<!DOCTYPE html>
<html lang="de">
<head>
<meta charset="utf-8">
<title>KOVALTEC – Visitenkarte</title>
<link rel="stylesheet" href="https://fonts.googleapis.com/css2?family=Mulish:wght@400;700;800&display=swap">
<style>
  :root {
    --backdrop: #e4e4e4;
    --card-black: #0b0b0b;
    --silver-light: #f2f2f2;
    --silver-mid: #aaaaaa;
    --silver-dark: #919191;
    --silver-text: #9d9d9d;
    --ink-white: #f4f4f4;
    --web-grey: #6a6a6a;
  }
  * { margin: 0; padding: 0; box-sizing: border-box; }
  html, body { width: 1200px; height: 1200px; overflow: hidden; }
  body {
    background: var(--backdrop);
    font-family: "Mulish", sans-serif;
    display: flex;
    flex-direction: column;
    align-items: center;
    justify-content: center;
    gap: 60px;
  }
  .card {
    position: relative;
    width: 840px;
    height: 480px;
    box-shadow: 0 10px 30px rgba(0,0,0,0.18);
    overflow: hidden;
  }
  .card-art { position: absolute; inset: 0; width: 100%; height: 100%; }
  .brand {
    position: absolute;
    display: flex;
    align-items: center;
    gap: 18px;
    color: var(--silver-mid);
    font-weight: 800;
    letter-spacing: 0.04em;
    white-space: nowrap;
  }
  .brand-square { background: var(--silver-mid); }
  .card--front .brand {
    left: 50%; top: 50%;
    transform: translate(-50%, -50%);
    font-size: 78px;
  }
  .card--front .brand-square { width: 64px; height: 64px; }
  .card--back .brand {
    left: 60px; top: 82px;
    font-size: 44px;
  }
  .card--back .brand-square { width: 38px; height: 38px; }
  .contact {
    position: absolute;
    right: 60px;
    top: 196px;
    text-align: right;
    color: var(--ink-white);
    font-size: 19px;
    line-height: 1.35;
    font-style: normal;
  }
  .contact-name { font-weight: 700; font-size: 20px; }
  .website {
    position: absolute;
    left: 0; right: 0;
    bottom: 20px;
    text-align: center;
    color: var(--web-grey);
    font-size: 20px;
    letter-spacing: 0.3em;
  }
</style>
</head>
<body>

  <section class="card card--front" aria-label="Vorderseite">
    <svg class="card-art" viewBox="0 0 840 480" preserveAspectRatio="none" aria-hidden="true">
      <defs>
        <linearGradient id="silver-front" x1="0" y1="0" x2="1" y2="1">
          <stop offset="0" stop-color="#f2f2f2"/>
          <stop offset="0.45" stop-color="#aaaaaa"/>
          <stop offset="0.6" stop-color="#f2f2f2"/>
          <stop offset="1" stop-color="#919191"/>
        </linearGradient>
      </defs>
      <rect width="840" height="480" fill="url(#silver-front)"/>
      <path d="M0,72 C280,18 560,18 840,62 L840,418 C560,468 280,468 0,408 Z" fill="none" stroke="#0b0b0b" stroke-width="3" transform="translate(0,-14)"/>
      <path d="M0,72 C280,18 560,18 840,62 L840,418 C560,468 280,468 0,408 Z" fill="#0b0b0b"/>
    </svg>
    <div class="brand"><span class="brand-square"></span>KOVALTEC</div>
  </section>

  <section class="card card--back" aria-label="Rückseite">
    <svg class="card-art" viewBox="0 0 840 480" preserveAspectRatio="none" aria-hidden="true">
      <defs>
        <linearGradient id="silver-back" x1="0" y1="0" x2="1" y2="1">
          <stop offset="0" stop-color="#919191"/>
          <stop offset="0.4" stop-color="#f2f2f2"/>
          <stop offset="0.7" stop-color="#aaaaaa"/>
          <stop offset="1" stop-color="#f2f2f2"/>
        </linearGradient>
      </defs>
      <rect width="840" height="480" fill="url(#silver-back)"/>
      <path d="M0,50 C280,12 560,12 840,46 L840,376 C560,426 280,426 0,366 Z" fill="none" stroke="#0b0b0b" stroke-width="3" transform="translate(0,14)"/>
      <path d="M0,50 C280,12 560,12 840,46 L840,376 C560,426 280,426 0,366 Z" fill="#0b0b0b"/>
    </svg>
    <div class="brand"><span class="brand-square"></span>KOVALTEC</div>
    <address class="contact">
      <div class="contact-name">Your Name</div>
      <div>Your Title</div>
      <div>Lindkofer Str. 18</div>
      <div>71468 Kernhausen</div>
      <div>Tel.: 07163-418259-0</div>
      <div>Name@kovaltec-pbz.de</div>
    </address>
    <div class="website">www.yourbusiness.com</div>
  </section>

</body>
</html>
```